Business cards real estate company

We need a design for a business card. It is a company that specializes in real estate sales. There should be space for a photo of the respective employee as well as the website and telephone number on it. Design should be noble, innovative.

Contact Information for Business Card

Website, Name, Position, Telefonnummer

Requirements
Must have
• Photo, logo

```html
<!DOCTYPE html>
<html lang="en">
<head>
<meta charset="utf-8">
<title>Domivera Business Card</title>
<link rel="stylesheet" href="https://fonts.googleapis.com/css2?family=Open+Sans:wght@400;600;700&family=Arimo:wght@400&display=swap">
<style>
  :root {
    --page-bg: #0c0c0c;
    --card-bg: #161616;
    --lime: #c2dc2c;
    --green: #6cbc44;
    --text-light: #e6e6e6;
    --rule: #5a5a5a;
    --photo-frame: #ffffff;
    --photo-tone: #8a8d90;
  }
  * { box-sizing: border-box; margin: 0; padding: 0; }
  html, body {
    width: 1200px;
    height: 900px;
    overflow: hidden;
    background: var(--page-bg);
  }
  .canvas {
    width: 1200px;
    height: 900px;
    display: flex;
    flex-direction: column;
    align-items: center;
    justify-content: center;
    gap: 40px;
  }
  .card {
    position: relative;
    width: 580px;
    height: 330px;
    background: var(--card-bg);
    box-shadow: 0 10px 28px rgba(0,0,0,0.6);
    overflow: hidden;
  }
  .card__stripe {
    position: absolute;
    left: 0; right: 0; bottom: 0;
    height: 9px;
    background: linear-gradient(90deg, var(--lime) 0%, var(--lime) 45%, var(--green) 100%);
  }
  .card--front {
    display: flex;
    align-items: center;
    justify-content: center;
  }
  .brand-name {
    font-family: "Open Sans", sans-serif;
    font-weight: 600;
    font-size: 62px;
    letter-spacing: 1px;
    color: var(--lime);
    margin-top: -10px;
  }
  .card--back {
    display: flex;
    flex-direction: column;
    align-items: center;
    padding-top: 36px;
  }
  .portrait {
    width: 150px;
    height: 150px;
    background: linear-gradient(180deg, var(--photo-frame) 0%, #d9dadb 55%, var(--photo-tone) 100%);
  }
  .person-name {
    margin-top: 8px;
    font-family: "Open Sans", sans-serif;
    font-weight: 600;
    font-size: 22px;
    letter-spacing: 0.5px;
    color: var(--lime);
    text-transform: uppercase;
  }
  .person-title {
    font-family: "Arimo", sans-serif;
    font-size: 15px;
    color: var(--text-light);
    margin-top: -2px;
  }
  .divider {
    width: 130px;
    height: 1px;
    background: var(--rule);
    margin: 9px 0 9px;
  }
  .contact-line {
    font-family: "Arimo", sans-serif;
    font-size: 15px;
    color: var(--text-light);
    letter-spacing: 0.3px;
  }
  .contact-line .accent { color: var(--green); }
</style>
</head>
<body>
<main class="canvas">
  <section class="card card--front">
    <h1 class="brand-name">Domivera</h1>
    <div class="card__stripe"></div>
  </section>

  <section class="card card--back">
    <div class="portrait" role="img" aria-label="Portrait photo of the employee"></div>
    <h2 class="person-name">Daniel Hartley</h2>
    <p class="person-title">Managing Director</p>
    <div class="divider"></div>
    <p class="contact-line">044-987 654 321 | www.<span class="accent">homeline</span>.com</p>
    <div class="card__stripe"></div>
  </section>
</main>
</body>
</html>
```